Design our branded business card!

We'd love for you to design our business card and come up with a fitting design that reflects the Pivex brand. We're a growing tech startup with big ambitions. We've included our brand guidelines (contain colour palette), logo (EPS vector in CMYK) and old designs to help you on your way.

We'd like to keep the design fairly simple:

* Name
* Phone number
* Email address
* Website (www.pivex.life)
* Twitter (@pivex)
* Address (18 Wexham Row, Leeds, UK, LS9 4ZQ).

This would need to include print and cutting marks.

If you have any questions just let us know!

Target Market(s)

Businesses, Press and our customers!

Industry/Entity Type

Business

Contact Information for Business Card

* Name
* Phone number
* Email address
* Twitter (@pivex)

Font styles to use
Sans Serif

Requirements
Must have
• 1. Must have the Pivex logo included.
• 2. Must use the font 'Brandon Text' in either 'light' or 'thin' (https://www.typevault-demo.com/fonts/qrsfonts/halden-sans/)
• 3. Must use exact colours references from the brand guidelines. Colours outside of the brand guidelines will be discounted. White (transparent) backgrounds are fine.
• 4. Must contain the following information:
• * Name
• * Phone number
• * Email address
• * Website (www.pivex.life)
• * Twitter (@pivex)
• * Address (18 Wexham Row, Leeds, UK, LS9 4ZQ).
Nice to have
• Must use the font 'Brandon Text' in either 'light' or 'thin' (https://www.typevault-demo.com/fonts/qrsfonts/halden-sans/)
Should not have
• Colours outside of the brand guidelines will be discounted. White (transparent) backgrounds are fine.
• Avoid creating icons or including photography.

```html
<!DOCTYPE html>
<html lang="en">
<head>
<meta charset="utf-8">
<title>Pivex Business Card</title>
<link rel="stylesheet" href="https://fonts.googleapis.com/css2?family=Didact+Gothic&family=Montserrat:wght@600&display=swap">
<style>
  :root {
    --stage: #161616;
    --card-light: #f1f1f1;
    --card-dark: #2d2f2f;
    --brand-green: #6aab48;
    --ink: #333333;
    --ink-soft: #444444;
    --paper-white: #f4f4f4;
    --rule: #bdbdbd;
    --crop-mark: #8a8a8a;
  }
  * { margin: 0; padding: 0; box-sizing: border-box; }
  html, body {
    width: 1200px; height: 1001px; overflow: hidden;
    background: var(--stage);
    font-family: "Didact Gothic", "Century Gothic", sans-serif;
  }
  .canvas { position: relative; width: 1200px; height: 1001px; }
  .crop-marks { position: absolute; left: 0; top: 0; width: 1200px; height: 1001px; pointer-events: none; }
  .crop-marks path { stroke: var(--crop-mark); stroke-width: 1; fill: none; }

  .card { position: absolute; left: 306px; width: 589px; height: 329px; }
  .card--front { top: 133px; background: var(--card-light); color: var(--ink); }
  .card--back { top: 539px; background: var(--card-dark); color: var(--paper-white); }

  .brand { position: absolute; display: flex; align-items: center; gap: 14px; }
  .brand__dot { width: 64px; height: 64px; border-radius: 50%; background: var(--brand-green); }
  .brand__name { font-size: 54px; line-height: 1; letter-spacing: 1px; }
  .card--front .brand { left: 173px; top: 110px; }
  .card--front .brand__name { color: var(--ink); }
  .card--back .brand { left: 171px; top: 133px; }
  .card--back .brand__name { color: var(--paper-white); }

  .holder { position: absolute; right: 392px; top: 239px; text-align: right; }
  .holder__name {
    font-family: "Montserrat", sans-serif; font-weight: 600;
    font-size: 16px; line-height: 20px; color: var(--ink); letter-spacing: 0.2px;
  }
  .holder__role { font-size: 14px; line-height: 18px; color: var(--ink-soft); }

  .rule { position: absolute; top: 241px; width: 1px; height: 44px; background: var(--rule); }
  .rule--one { left: 220px; }
  .rule--two { left: 402px; }

  .contact, .address {
    position: absolute; top: 240px; list-style: none;
    font-size: 14px; line-height: 16.5px; color: var(--ink);
  }
  .contact { left: 243px; }
  .address { left: 424px; }
  .contact__label { color: var(--brand-green); font-weight: 700; }

  .back-url {
    position: absolute; left: 0; right: 0; top: 271px;
    text-align: center; font-size: 14px; color: var(--paper-white); letter-spacing: 0.3px;
  }
</style>
</head>
<body>
<main class="canvas">
  <section class="card card--front">
    <div class="brand">
      <span class="brand__dot"></span>
      <span class="brand__name">pivex</span>
    </div>
    <div class="holder">
      <p class="holder__name">DANA WHITFIELD</p>
      <p class="holder__role">Marketing</p>
    </div>
    <span class="rule rule--one"></span>
    <ul class="contact">
      <li><span class="contact__label">T:</span> 0113 496 0721</li>
      <li><span class="contact__label">E:</span> dana@pivex.life</li>
      <li><span class="contact__label">W:</span> www.pivex.life</li>
    </ul>
    <span class="rule rule--two"></span>
    <ul class="address">
      <li>18 Wexham Row, Leeds</li>
      <li>UK, LS9 4ZQ</li>
      <li><span class="contact__label">Tw:</span> @pivex</li>
    </ul>
  </section>

  <section class="card card--back">
    <div class="brand">
      <span class="brand__dot"></span>
      <span class="brand__name">pivex</span>
    </div>
    <p class="back-url">www.pivex.life</p>
  </section>

  <svg class="crop-marks" viewBox="0 0 1200 1001" aria-hidden="true">
    <path d="M284 133H300M306 111V127 M901 133H917M895 111V127 M284 462H300M306 468V484 M901 462H917M895 468V484"/>
    <path d="M284 539H300M306 517V533 M901 539H917M895 517V533 M284 868H300M306 874V890 M901 868H917M895 874V890"/>
  </svg>
</main>
</body>
</html>
```